Chiropractic healthcare group business card

We are a Portland Oregon based chiropractic healthcare group. Looking for a new business card design. Something cutting edge, that shows off our new logo and tag line.Use either of the attached logos.Our tag line = "Who would you be without pain?"I'm open to about anything, impress me!!
Target Market(s)
Chiropractic patients - Auto injury, back pain, sports injuries, neck , shoulder, hip, knee, ankle pain.
Industry/Entity Type
Chiropractic
Contact Information for Business Card
Dr. Bram Holtvick, D.C.
Clinic name - Fernway Chiropractic
2 clinics
location #1
20418 NW Marwick Road
Suite B
North Plains, OR 97133
Location #2
13529 SE Calloway Street
Portland OR 97236
Main phone line 971.555.0143
website : www.FernwayClinics.example
Tag line "Who would you be without pain?"
Colors
Designer to choose colors to be used in the design.
Requirements
Must have
- Use the logo colors -- Want the orange color to be a TRUE orange.
- Both clinic address
- phone number
- website
- personal email - b.holtvick@ReliefBeginsHere.example
- tag line - "Who would you be without pain?"

```html
<!DOCTYPE html>
<html lang="en">
<head>
<meta charset="utf-8">
<title>Fernway Chiropractic Business Card</title>
<link rel="stylesheet" href="https://fonts.googleapis.com/css2?family=Source+Sans+3:wght@400;600;700&family=Roboto+Condensed:wght@400;500&display=swap">
<style>
  :root {
    --orange: #e99a42;
    --charcoal: #606060;
    --white: #ffffff;
    --backdrop: #a3a3a3;
    --ink: #3d3d3d;
  }
  * { margin: 0; padding: 0; box-sizing: border-box; }
  html, body { width: 1200px; height: 1045px; overflow: hidden; }
  body {
    background: var(--backdrop);
    position: relative;
    font-family: "Source Sans 3", Arial, sans-serif;
  }
  .card {
    position: absolute;
    top: 85px;
    width: 471px;
    height: 853px;
    background: var(--white);
    overflow: hidden;
  }
  .card--front { left: 105px; }
  .card--back { left: 645px; }

  /* Front */
  .front__band {
    position: absolute; left: 0; right: 0; top: 617px; bottom: 0;
    background: var(--charcoal);
  }
  .front__panel {
    position: absolute; left: 26px; top: 24px; width: 422px; height: 804px;
    background: var(--orange);
    text-align: center;
  }
  .wordmark {
    font-family: "Source Sans 3", Arial, sans-serif;
    font-weight: 700;
    text-transform: uppercase;
    line-height: 1;
  }
  .wordmark__name { display: block; font-size: 46px; letter-spacing: 0.32em; padding-left: 0.32em; }
  .wordmark__sub { display: block; font-size: 18px; letter-spacing: 0.16em; padding-left: 0.16em; margin-top: 14px; }
  .front__wordmark { position: absolute; left: 0; right: 0; top: 305px; color: var(--charcoal); }
  .front__name {
    position: absolute; left: 0; right: 0; top: 584px;
    font-family: "Roboto Condensed", Arial, sans-serif; font-weight: 500;
    font-size: 28px; letter-spacing: 0.06em; color: var(--white);
  }
  .front__title {
    position: absolute; left: 0; right: 0; top: 630px;
    font-family: "Roboto Condensed", Arial, sans-serif;
    font-size: 23px; letter-spacing: 0.1em; color: var(--white);
  }
  .front__web {
    position: absolute; left: 0; right: 0; top: 734px;
    font-family: "Roboto Condensed", Arial, sans-serif; font-weight: 500;
    font-size: 23px; letter-spacing: 0.06em; color: var(--charcoal);
  }

  /* Back */
  .back__wordmark { position: absolute; left: 0; right: 0; top: 192px; text-align: center; color: var(--charcoal); }
  .back__wordmark .wordmark__name { font-size: 34px; }
  .back__wordmark .wordmark__sub { font-size: 14px; margin-top: 12px; }
  .location { position: absolute; left: 99px; color: var(--ink); font-size: 23px; letter-spacing: 0.1em; line-height: 29px; }
  .location--north { top: 302px; }
  .location--portland { top: 448px; }
  .location__label { color: var(--orange); display: flex; align-items: center; gap: 5px; margin-left: -21px; }
  .location__label svg { width: 16px; height: 21px; }
  .contact { position: absolute; left: 80px; display: flex; align-items: center; gap: 8px; color: var(--ink); }
  .contact svg { width: 18px; height: 18px; flex: none; }
  .contact--phone { top: 573px; font-size: 23px; letter-spacing: 0.12em; }
  .contact--phone svg { margin-top: 6px; }
  .contact--email { top: 612px; font-size: 17px; letter-spacing: 0.04em; }
  .back__stripe { position: absolute; left: 0; right: 0; top: 686px; height: 13px; }
  .back__tagline {
    position: absolute; left: 0; right: 0; top: 726px; text-align: center;
    color: var(--orange); font-weight: 700; font-size: 26px; letter-spacing: 0.1em; line-height: 37px;
  }
</style>
</head>
<body>
  <section class="card card--front">
    <div class="front__band"></div>
    <div class="front__panel">
      <div class="wordmark front__wordmark">
        <span class="wordmark__name">Fernway</span>
        <span class="wordmark__sub">Chiropractic</span>
      </div>
      <p class="front__name">Dr. Bram Holtvick, D.C.</p>
      <p class="front__title">Director</p>
      <p class="front__web">www.FernwayClinics.example</p>
    </div>
  </section>

  <section class="card card--back">
    <div class="wordmark back__wordmark">
      <span class="wordmark__name">Fernway</span>
      <span class="wordmark__sub">Chiropractic</span>
    </div>

    <div class="location location--north">
      <p class="location__label">
        <svg viewBox="0 0 16 21" aria-hidden="true"><path d="M8 0a7 7 0 0 0-7 7c0 5 7 14 7 14s7-9 7-14a7 7 0 0 0-7-7zm0 10a3 3 0 1 1 0-6 3 3 0 0 1 0 6z" fill="var(--orange)"/></svg>
        _NORTH PLAINS
      </p>
      <p>20418 NW Marwick Road</p>
      <p>Suite B</p>
      <p>North Plains, OR 97133</p>
    </div>

    <div class="location location--portland">
      <p class="location__label">
        <svg viewBox="0 0 16 21" aria-hidden="true"><path d="M8 0a7 7 0 0 0-7 7c0 5 7 14 7 14s7-9 7-14a7 7 0 0 0-7-7zm0 10a3 3 0 1 1 0-6 3 3 0 0 1 0 6z" fill="var(--orange)"/></svg>
        _PORTLAND
      </p>
      <p>13529 SE Calloway Street</p>
      <p>Portland OR 97236</p>
    </div>

    <p class="contact contact--phone">
      <svg viewBox="0 0 24 24" aria-hidden="true"><path d="M6.6 10.8a15.1 15.1 0 0 0 6.6 6.6l2.2-2.2a1 1 0 0 1 1-.25 11.4 11.4 0 0 0 3.6.57 1 1 0 0 1 1 1V20a1 1 0 0 1-1 1A17 17 0 0 1 3 4a1 1 0 0 1 1-1h3.5a1 1 0 0 1 1 1c0 1.25.2 2.45.57 3.57a1 1 0 0 1-.25 1z" fill="var(--orange)"/></svg>
      971.555.0143
    </p>

    <p class="contact contact--email">
      <svg viewBox="0 0 24 24" aria-hidden="true"><path d="M3 5h18a1 1 0 0 1 1 1v12a1 1 0 0 1-1 1H3a1 1 0 0 1-1-1V6a1 1 0 0 1 1-1zm1 2.4V17h16V7.4l-8 5.3z M5 7l7 4.6L19 7z" fill="var(--orange)"/></svg>
      b.holtvick@ReliefBeginsHere.example
    </p>

    <svg class="back__stripe" viewBox="0 0 471 13" preserveAspectRatio="none" aria-hidden="true">
      <rect width="471" height="13" fill="var(--charcoal)"/>
      <polygon points="0,0 203,0 212,13 0,13" fill="var(--orange)"/>
    </svg>

    <p class="back__tagline">Who would you be<br>without pain?</p>
  </section>
</body>
</html>
```